Business Card Design

I would like a new business card design for an accounting firm that specializes in resolving clients tax problems. I want the card to give the impression that we are not your typical stodgy accounting firm, but at the same time we will get the job done.
Industry/Entity Type
Business
Contact Information for Business Card
Dorian T Welsby
Certified Public Accountant
38-27 52nd Street
Sunnyside, NY 11287
Tel: (718) 555-0142
Fax: (888) 555-0199
e-mail: dtwthecpa@ledgerpost.com
website: harborfilingreliefexperts.com

```html
<!DOCTYPE html>
<html lang="en">
<head>
<meta charset="utf-8">
<title>Dorian T Welsby – Business Card</title>
<link rel="stylesheet" href="https://fonts.googleapis.com/css2?family=Zilla+Slab:wght@700&family=Oswald:wght@500&family=Arimo:wght@400&family=Archivo+Black&display=swap">
<style>
  :root {
    --stage: #7f7f7f;
    --paper: #ffffff;
    --navy: #1e3c6c;
    --navy-edge: #c9d3e2;
    --gold: #f2c21b;
    --ink: #1a1a1a;
    --art-red: #f2a0a0;
    --art-light: #e3edf3;
    --art-warm: #f4d6b8;
  }
  * { box-sizing: border-box; margin: 0; padding: 0; }
  html, body { width: 1200px; height: 1200px; overflow: hidden; }
  body { background: var(--stage); position: relative; font-family: "Arimo", Arial, sans-serif; }

  .card {
    position: absolute;
    background: var(--paper);
    box-shadow: 0 2px 6px rgba(0,0,0,0.25);
    overflow: hidden;
  }
  .card--front { left: 40px; top: 60px; width: 720px; height: 424px; }
  .card--back  { left: 352px; top: 510px; width: 720px; height: 424px; }

  .side-label {
    position: absolute;
    font-family: "Archivo Black", Arial, sans-serif;
    font-size: 60px;
    color: var(--ink);
    letter-spacing: 1px;
  }
  .side-label--front { left: 820px; top: 225px; }
  .side-label--back  { left: 82px; top: 680px; }

  .tax-art {
    position: absolute;
    left: 430px; top: 22px;
    width: 270px; height: 296px;
    border-radius: 50%;
    background: radial-gradient(circle at 60% 40%, var(--art-warm) 0%, var(--art-light) 45%, var(--art-red) 80%, rgba(242,160,160,0.4) 100%);
  }

  .name-banner {
    position: absolute;
    left: 30px; top: 78px;
    width: 458px; height: 112px;
    background: var(--navy);
    border: 3px solid var(--navy-edge);
    outline: 2px solid var(--navy);
    border-radius: 12px;
    text-align: center;
    padding-top: 8px;
  }
  .name-banner__name {
    font-family: "Zilla Slab", Georgia, serif;
    font-weight: 700;
    font-size: 44px;
    color: #fff;
    letter-spacing: 2px;
    line-height: 1.15;
    white-space: nowrap;
  }
  .name-banner__title {
    font-family: "Oswald", "Arial Narrow", sans-serif;
    font-weight: 500;
    font-size: 25px;
    color: var(--gold);
    letter-spacing: 3px;
    line-height: 1.4;
    white-space: nowrap;
  }

  .contact { position: absolute; font-size: 23px; color: var(--ink); line-height: 1.32; font-style: normal; white-space: nowrap; }
  .contact--address { left: 150px; top: 232px; }
  .contact--phones { left: 22px; top: 340px; }
  .contact--online { right: 24px; top: 340px; text-align: right; }
</style>
</head>
<body>
  <section class="card card--front" aria-label="Business card front">
    <div class="tax-art" role="img" aria-label="Illustration of a prohibition sign over a hand signing a tax payment cheque"></div>

    <div class="name-banner">
      <div class="name-banner__name">DORIAN T. WELSBY</div>
      <div class="name-banner__title">CERTIFIED PUBLIC ACCOUNTANT</div>
    </div>

    <address class="contact contact--address">
      38-27 52nd Street<br>Sunnyside, NY 11287
    </address>
    <div class="contact contact--phones">
      Tel: (718) 555-0142<br>Fax: (888) 555-0199
    </div>
    <div class="contact contact--online">
      dtwthecpa@ledgerpost.com<br>harborfilingreliefexperts.com
    </div>
  </section>
  <div class="side-label side-label--front">FRONT</div>

  <section class="card card--back" aria-label="Business card back"></section>
  <div class="side-label side-label--back">BACK</div>
</body>
</html>
```